"End of year wishes" - Electronic card

Velmora is a regulatory consulting company in the cosmetic sector. We provide premium services and have 12 years of experience.
Please visit our website for more information: https://velmora-example.com
Like every year, we would like to send an electronic design to our clients and partners to wish them happy holidays. This year, we would like to share two good news with them: offer them a surprise (to be revealed later on) and invite them to visit our new brand new website. We relay on your talent and imagination for the design! We need something very professional, serious, beautiful and in line with our graphic layout (see our company website)

Target Market(s)

cosmetic brands

Industry/Entity Type

Cosmetics

Requirements
Must have
• The following statement should be included to the design:

We wish you a Happy Holiday and a Marvelous New Year 2021!
As December is the month of giving, we have a surprise for you. Please contact your dedicated Account Manager to find out more!

Good news never comes alone, we've also updated our website in order to serve you better. We hope you like it as much as we do.
Please enjoy the experience: www.velmora-example.com

```html
<!DOCTYPE html>
<html lang="en">
<head>
<meta charset="utf-8">
<title>Velmora – Season's Greetings 2021</title>
<link rel="stylesheet" href="https://fonts.googleapis.com/css2?family=Poppins:wght@400;600&family=Yellowtail&display=swap">
<style>
  :root {
    --frame-green: #94d600;
    --title-green: #8ccf0e;
    --accent-green: #8cc63f;
    --ink: #333333;
    --flake-grey: #6d6e71;
    --dot-grey: #a7a9ac;
    --paper: #ffffff;
  }
  * { margin: 0; padding: 0; box-sizing: border-box; }
  html, body { width: 1200px; height: 919px; overflow: hidden; background: var(--paper); }
  .canvas { position: relative; width: 1200px; height: 919px; background: var(--paper); }
  .card {
    position: absolute; left: 91px; top: 61px; width: 1014px; height: 787px;
    border: 20px solid var(--frame-green); background: var(--paper);
    box-shadow: 0 6px 28px rgba(0,0,0,0.18);
  }
  .decor { position: absolute; inset: 0; }
  .greeting {
    position: absolute; left: 0; width: 1200px; top: 205px; text-align: center;
    font-family: "Yellowtail", cursive; color: var(--title-green);
    font-size: 46px; line-height: 58px; letter-spacing: 0.2px;
  }
  .message {
    position: absolute; left: 0; width: 1200px; text-align: center;
    font-family: "Poppins", sans-serif; font-size: 15.5px; color: var(--ink);
    line-height: 37px;
  }
  .message--surprise { top: 383px; }
  .message--website { top: 494px; }
  .message--visit { top: 605px; font-weight: 600; }
  .highlight { color: var(--accent-green); font-weight: 600; }
  .sleigh-art {
    position: absolute; left: 473px; top: 693px; width: 220px; height: 48px;
    background: linear-gradient(90deg, #8cc63f, #a3d65c);
    border-radius: 8px; opacity: 0.85;
  }
</style>
</head>
<body>
<main class="canvas">
  <div class="card"></div>

  <svg class="decor" width="1200" height="919" viewBox="0 0 1200 919">
    <g class="snowflake-art">
      <circle role="img" aria-label="Large green snowflake ornament" cx="184" cy="256" r="62" fill="#8cc63f" opacity="0.22"/>
      <circle role="img" aria-label="Small green snowflake ornament" cx="289" cy="153" r="22" fill="#8cc63f" opacity="0.22"/>
      <circle role="img" aria-label="Grey snowflake ornament" cx="230" cy="412" r="40" fill="#6d6e71" opacity="0.18"/>
      <circle role="img" aria-label="Small green snowflake ornament" cx="167" cy="502" r="22" fill="#8cc63f" opacity="0.22"/>
      <circle role="img" aria-label="Small grey snowflake ornament" cx="236" cy="548" r="17" fill="#6d6e71" opacity="0.18"/>
      <circle role="img" aria-label="Tiny green snowflake ornament" cx="190" cy="630" r="13" fill="#8cc63f" opacity="0.22"/>
      <circle role="img" aria-label="Grey snowflake ornament" cx="948" cy="169" r="42" fill="#6d6e71" opacity="0.18"/>
      <circle role="img" aria-label="Small green snowflake ornament" cx="994" cy="263" r="22" fill="#8cc63f" opacity="0.22"/>
      <circle role="img" aria-label="Large green snowflake ornament" cx="991" cy="381" r="58" fill="#8cc63f" opacity="0.22"/>
      <circle role="img" aria-label="Small grey snowflake ornament" cx="962" cy="502" r="17" fill="#6d6e71" opacity="0.18"/>
      <circle role="img" aria-label="Small green snowflake ornament" cx="1016" cy="566" r="22" fill="#8cc63f" opacity="0.22"/>
    </g>
    <g class="snow-rings" fill="none" stroke-width="1.6">
      <circle cx="163" cy="146" r="5.5" stroke="var(--accent-green)"/>
      <circle cx="154" cy="371" r="5.5" stroke="var(--dot-grey)"/>
      <circle cx="256" cy="596" r="5.5" stroke="var(--accent-green)"/>
      <circle cx="1039" cy="483" r="5.5" stroke="var(--dot-grey)"/>
    </g>
    <g class="snow-dots">
      <circle cx="360" cy="142" r="5" fill="var(--dot-grey)"/>
      <circle cx="239" cy="171" r="2.5" fill="var(--dot-grey)"/>
      <circle cx="812" cy="164" r="5.5" fill="var(--accent-green)"/>
      <circle cx="851" cy="139" r="2.5" fill="var(--dot-grey)"/>
      <circle cx="1029" cy="161" r="5.5" fill="var(--dot-grey)"/>
      <circle cx="271" cy="326" r="2.5" fill="var(--accent-green)"/>
      <circle cx="901" cy="364" r="2.5" fill="var(--accent-green)"/>
      <circle cx="146" cy="432" r="2.5" fill="var(--accent-green)"/>
      <circle cx="927" cy="463" r="2.5" fill="var(--accent-green)"/>
      <circle cx="271" cy="483" r="2.5" fill="var(--dot-grey)"/>
      <circle cx="171" cy="575" r="2.5" fill="var(--accent-green)"/>
      <circle cx="943" cy="575" r="2.5" fill="var(--dot-grey)"/>
      <circle cx="1051" cy="629" r="2.5" fill="var(--accent-green)"/>
      <circle cx="976" cy="643" r="6" fill="var(--accent-green)"/>
      <circle cx="157" cy="682" r="2.5" fill="var(--dot-grey)"/>
      <circle cx="226" cy="685" r="1.5" fill="var(--accent-green)"/>
      <circle cx="196" cy="714" r="1.5" fill="var(--accent-green)"/>
      <circle cx="1013" cy="697" r="1.5" fill="var(--dot-grey)"/>
    </g>
  </svg>

  <h1 class="greeting">We wish you a Happy Holiday and<br>a Marvelous New Year 2021!</h1>

  <p class="message message--surprise">As December is the month of giving, <span class="highlight">we have a surprise for you.</span><br>Please contact your dedicated Account Manager to find out more!</p>

  <p class="message message--website">Good news never comes alone, we've also updated our website<br>in order to serve you better. We hope you like it as much as we do.</p>

  <p class="message message--visit">Please enjoy the experience: <span class="highlight">www.velmora-example.com</span></p>

  <div class="sleigh-art" role="img" aria-label="Illustration of Santa's sleigh pulled by three reindeer"></div>
</main>
</body>
</html>
```